Equity, Effectiveness and Efficiency in charitable food relief sector

I am undertaking my PhD in food policy in the charitable food relief sector, specifically investigating the factors (supply, demand and capacity) that affect the introduction of nutrition policy and in turn, affect the sector's ability to achieve equity, effectiveness and efficiency.

I need a graphic device that incorporates this central idea of Equity, Effectiveness and Efficiency, and how the factors of supply, demand and capacity interact. There are sub-factors within supply (1-6), demand (7-10) and capacity (11 - 15). All these details are shown in the attached figure (Basic figure_Eq Effec Effic and factors.jpg)

This figure (Basic figure_Eq Effec Effic and factors.jpg) contains all the information I need in a graphic but I need something that is more visually appealing, and that can link the ideas in a format other than a table. The final graphic will outline how the food relief sector balances the core objectives of equity, effectiveness and efficiency with the factors (and sub-factors) of supply, demand and capacity.

```html
<!DOCTYPE html>
<html lang="en">
<head>
<meta charset="utf-8">
<title>Equity, Effectiveness, Efficiency – Factors</title>
<link href="https://fonts.googleapis.com/css2?family=Montserrat:wght@400;500;700&display=swap" rel="stylesheet">
<style>
  :root {
    --ink: #1f1f1f;
    --frame: #8a8a8a;
    --orange: #f7860f;
    --orange-deep: #d8620a;
    --teal: #00abd0;
    --teal-deep: #0087a6;
    --purple: #6b2a8e;
    --purple-deep: #4a1c6c;
    --line: #333;
    --paper: #ffffff;
  }
  * { box-sizing: border-box; margin: 0; padding: 0; }
  html, body { width: 689px; height: 1200px; overflow: hidden; background: var(--paper); }
  body { font-family: "Montserrat", Arial, sans-serif; color: var(--ink); }
  .canvas { position: relative; width: 689px; height: 1200px; }
  .connectors { position: absolute; inset: 0; }

  .core-title {
    position: absolute; left: 240px; top: 64px; width: 160px;
    text-align: center; font-weight: 400; font-size: 12.6px; line-height: 16.6px; letter-spacing: 0.2px;
  }
  .core-sub {
    position: absolute; left: 250px; top: 116px; width: 140px;
    text-align: center; font-size: 7px; line-height: 12.3px; font-weight: 500;
  }

  .pillar {
    position: absolute; top: 242px; width: 151px; height: 71px;
    border: 0.6px solid var(--frame); border-radius: 6px; background: var(--paper);
  }
  .pillar-inner {
    position: absolute; left: 5.5px; top: 4.5px; width: 139px; height: 62px;
    border: 4px solid; border-radius: 6px; display: flex; align-items: center;
  }
  .pillar-icon { width: 38px; height: 38px; border-radius: 50%; margin-left: 6px; flex: none; }
  .pillar-name { font-weight: 700; font-size: 14px; letter-spacing: 0.2px; margin-left: 8px; }
  .supply .pillar-inner { border-color: var(--orange); border-bottom-color: var(--orange-deep); }
  .supply .pillar-icon { background: #fde3c6; }
  .demand .pillar-inner { border-color: var(--teal); border-bottom-color: var(--teal-deep); }
  .demand .pillar-icon { background: #cdeef6; }
  .capacity .pillar-inner { border-color: var(--purple); border-bottom-color: var(--purple-deep); }
  .capacity .pillar-icon { background: #e4d5ec; }

  .factor {
    position: absolute; width: 112px; height: 53px;
    border: 0.6px solid var(--frame); border-radius: 6px; background: var(--paper);
  }
  .factor-inner {
    position: absolute; left: 3.5px; top: 3px; width: 103.5px; height: 46px;
    border: 3.4px solid; border-radius: 6px;
    display: flex; flex-direction: column; align-items: center; justify-content: center;
    text-align: center;
  }
  .factor-name { font-size: 7.6px; line-height: 9px; font-weight: 400; }
  .factor-num { font-size: 7.6px; line-height: 9px; margin-top: 3px; }
  .s .factor-inner { border-color: var(--orange); border-bottom-color: var(--orange-deep); }
  .s .factor-num { color: var(--orange); }
  .d .factor-inner { border-color: var(--teal); border-bottom-color: var(--teal-deep); }
  .d .factor-num { color: var(--teal); }
  .c .factor-inner { border-color: var(--purple); border-bottom-color: var(--purple-deep); }
  .c .factor-num { color: var(--purple); }
  .s { left: 87.5px; }
  .d { left: 282.5px; }
  .c1 { left: 477.5px; }
  .c2 { left: 530.5px; }
</style>
</head>
<body>
<div class="canvas">
  <svg class="connectors" width="689" height="1200" viewBox="0 0 689 1200" aria-hidden="true">
    <circle cx="320" cy="104" r="83" fill="#fff" stroke="#8a8a8a" stroke-width="0.6"/>
    <path d="M251.2 71.6 A76 76 0 0 1 392.7 81.8" fill="none" stroke="#f7860f" stroke-width="4"/>
    <path d="M392.7 81.8 A76 76 0 0 1 320 180" fill="none" stroke="#5a2180" stroke-width="4"/>
    <path d="M320 180 A76 76 0 0 1 251.2 71.6" fill="none" stroke="#0a9cc0" stroke-width="4"/>
    <g fill="none" stroke="#333" stroke-width="0.7" stroke-dasharray="2.6 1.6">
      <path d="M237 104 H114 V246"/>
      <path d="M405 104 H513 V246"/>
      <path d="M321 188 V245"/>
      <path d="M68 313 V702.5"/>
      <path d="M68 362 H88 M68 431 H88 M68 500 H88 M68 569 H88 M68 638 H88 M68 702.5 H88"/>
      <path d="M267 313 V566"/>
      <path d="M267 362 H283 M267 431 H283 M267 500 H283 M267 566 H283"/>
      <path d="M462 313 V1124.5"/>
      <path d="M462 362 H478 M462 431 H531 M462 500 H531 M462 566 H478 M462 638 H478 M462 702.5 H531 M462 775 H531 M462 849 H531 M462 916 H531 M462 992 H531 M462 1061.5 H478 M462 1124.5 H478"/>
    </g>
  </svg>

  <h1 class="core-title">EQUITY,<br>EFFECTIVENESS,<br>EFFICIENCY</h1>
  <p class="core-sub">Factors affecting the introduction<br>of nutrition policy</p>

  <div class="pillar supply" style="left:47px">
    <div class="pillar-inner">
      <div class="pillar-icon" role="img" aria-label="Supply icon: delivery truck, gear and person"></div>
      <span class="pillar-name">SUPPLY</span>
    </div>
  </div>
  <div class="pillar demand" style="left:242.3px">
    <div class="pillar-inner">
      <div class="pillar-icon" role="img" aria-label="Demand icon: analysis chart with magnifier"></div>
      <span class="pillar-name">DEMAND</span>
    </div>
  </div>
  <div class="pillar capacity" style="left:437.7px">
    <div class="pillar-inner">
      <div class="pillar-icon" role="img" aria-label="Capacity icon: person inside a segmented ring"></div>
      <span class="pillar-name">CAPACITY</span>
    </div>
  </div>

  <div class="factor s" style="top:335.5px"><div class="factor-inner"><span class="factor-name">Uncertain material<br>supply</span><span class="factor-num">01</span></div></div>
  <div class="factor s" style="top:404.6px"><div class="factor-inner"><span class="factor-name">Uncertain Monetary<br>Supply</span><span class="factor-num">02</span></div></div>
  <div class="factor s" style="top:473.7px"><div class="factor-inner"><span class="factor-name">Limited food<br>supply</span><span class="factor-num">03</span></div></div>
  <div class="factor s" style="top:542.8px"><div class="factor-inner"><span class="factor-name">perishability</span><span class="factor-num" style="margin-top:8px">04</span></div></div>
  <div class="factor s" style="top:611.4px"><div class="factor-inner"><span class="factor-name">Donor<br>Constraints</span><span class="factor-num">05</span></div></div>
  <div class="factor s" style="top:676.2px"><div class="factor-inner"><span class="factor-name">Donor<br>Relationships</span><span class="factor-num">06</span></div></div>

  <div class="factor d" style="top:335.5px"><div class="factor-inner"><span class="factor-name">Uncertain<br>Demand</span><span class="factor-num">07</span></div></div>
  <div class="factor d" style="top:404.6px"><div class="factor-inner"><span class="factor-name">Limited demand<br>visibility</span><span class="factor-num">08</span></div></div>
  <div class="factor d" style="top:473.7px"><div class="factor-inner"><span class="factor-name">Clients<br>Choice</span><span class="factor-num">09</span></div></div>
  <div class="factor d" style="top:542.8px"><div class="factor-inner"><span class="factor-name">Food<br>Wastage</span><span class="factor-num">10</span></div></div>

  <div class="factor c c1" style="top:335.5px"><div class="factor-inner"><span class="factor-name">Storage</span><span class="factor-num" style="margin-top:8px">11</span></div></div>
  <div class="factor c c2" style="top:404.6px"><div class="factor-inner"><span class="factor-name">Cold</span><span class="factor-num" style="margin-top:8px">11 .a</span></div></div>
  <div class="factor c c2" style="top:473.7px"><div class="factor-inner"><span class="factor-name">Warehouse</span><span class="factor-num" style="margin-top:8px">11 .b</span></div></div>
  <div class="factor c c1" style="top:542.8px"><div class="factor-inner"><span class="factor-name">Transporation</span><span class="factor-num" style="margin-top:8px">12</span></div></div>
  <div class="factor c c1" style="top:611.4px"><div class="factor-inner"><span class="factor-name">Workforce</span><span class="factor-num" style="margin-top:8px">13</span></div></div>
  <div class="factor c c2" style="top:680.5px"><div class="factor-inner"><span class="factor-name">Volunteers</span><span class="factor-num" style="margin-top:8px">13 .a</span></div></div>
  <div class="factor c c2" style="top:749.6px"><div class="factor-inner"><span class="factor-name">Storage</span><span class="factor-num" style="margin-top:8px">13 .b</span></div></div>
  <div class="factor c c2" style="top:822.5px"><div class="factor-inner"><span class="factor-name">Storage</span><span class="factor-num" style="margin-top:8px">13 .c</span></div></div>
  <div class="factor c c2" style="top:891.5px"><div class="factor-inner"><span class="factor-name">Storage</span><span class="factor-num" style="margin-top:8px">13 .d</span></div></div>
  <div class="factor c c2" style="top:962px"><div class="factor-inner"><span class="factor-name">Storage</span><span class="factor-num" style="margin-top:8px">13 .e</span></div></div>
  <div class="factor c c1" style="top:1032.1px"><div class="factor-inner"><span class="factor-name">External stakeholders</span><span class="factor-num" style="margin-top:8px">14</span></div></div>
  <div class="factor c c1" style="top:1097.8px"><div class="factor-inner"><span class="factor-name">Budget</span><span class="factor-num" style="margin-top:8px">15</span></div></div>
</div>
</body>
</html>
```